Website redesign

Looking to redesign our existing website. (quill7meadows.com.au)
New design needs to be bright, fun and have an easy flowing.
The website needs to be design with call to action.

Some examples of other websites:
fernquaylo.com
tovanmilk.com.au

We are happy with the content of our existing website.

Target Market(s)

other businesses

Industry/Entity Type

Business Service

Number of Pages Required

5+ page

Requirements
Must have
• Theme redesign
Cool animation similar to fernquaylo.com

```html
<!DOCTYPE html>
<html lang="en">
<head>
<meta charset="utf-8">
<title>Quill 7 Meadows – Mortgage Broking</title>
<link href="https://fonts.googleapis.com/css2?family=IBM+Plex+Sans:wght@400;500;600;700&display=swap" rel="stylesheet">
<style>
  :root {
    --brand-blue: #1b96d9;
    --ink: #14202b;
    --text: #222;
    --white: #fff;
    --footer-bg: #2a2a2a;
    --footer-line: #4a4a4a;
  }
  * { margin: 0; padding: 0; box-sizing: border-box; }
  html, body { width: 914px; height: 1200px; overflow: hidden; }
  body {
    position: relative;
    font-family: "IBM Plex Sans", sans-serif;
    color: var(--text);
    background: var(--white);
  }
  .abs { position: absolute; }

  /* Header */
  .site-header { position: absolute; left: 0; top: 0; width: 914px; height: 90px; background: var(--white); }
  .brand { position: absolute; display: flex; align-items: center; gap: 8px; }
  .brand-dot { border-radius: 50%; flex: none; }
  .brand-name { font-weight: 600; line-height: 1; }
  .header-brand { left: 99px; top: 14px; }
  .header-brand .brand-dot { width: 14px; height: 14px; background: var(--brand-blue); }
  .header-brand .brand-name { color: var(--ink); font-size: 22px; }
  .header-brand .brand-name span { display: block; }
  .header-brand .brand-name .top { font-size: 34px; margin-bottom: 4px; }

  .quote-btn {
    left: 565px; top: 19px; width: 93px; height: 27px;
    background: var(--brand-blue); color: var(--white);
    border-radius: 3px; font-size: 10px; font-weight: 600;
    display: flex; align-items: center; justify-content: center; letter-spacing: .3px;
  }
  .call-icon { left: 676px; top: 21px; }
  .call-label { left: 709px; top: 17px; font-size: 11px; color: var(--ink); }
  .call-number { left: 709px; top: 31px; font-size: 17px; font-weight: 500; color: var(--brand-blue); }

  .main-nav a {
    position: absolute; top: 63px; font-size: 11px; font-weight: 500;
    color: var(--ink); text-decoration: none; letter-spacing: .2px;
  }

  /* Hero */
  .hero {
    left: 0; top: 90px; width: 914px; height: 340px;
    background: linear-gradient(100deg, #9fb1c6 0%, #b7c4d3 35%, #c8cfd6 55%, #8f9aa7 80%, #6a717b 100%);
  }
  .hero-title {
    left: 100px; top: 212px; color: var(--white);
    font-size: 34px; font-weight: 700; line-height: 41px; letter-spacing: .5px;
  }

  /* Content */
  .content-photo {
    left: 0; top: 430px; width: 914px; height: 505px;
    background: linear-gradient(90deg, #fafbfc 0%, #f4f5f7 45%, #dfe3e8 62%, #b9c0c9 78%, #8e98a6 100%);
  }
  .section-title { left: 99px; top: 473px; font-size: 18px; font-weight: 700; color: #111; letter-spacing: .2px; }
  .section-rule { left: 100px; top: 504px; width: 33px; height: 2px; background: var(--brand-blue); }
  .body-copy { left: 99px; width: 350px; font-size: 9.2px; line-height: 13.4px; color: var(--text); }

  /* Footer */
  .site-footer { left: 0; top: 935px; width: 914px; height: 265px; background: var(--footer-bg); color: var(--white); }
  .footer-brand { left: 97px; top: 985px; }
  .footer-brand .brand-dot { width: 18px; height: 18px; background: var(--white); }
  .footer-brand .brand-name { color: var(--white); font-size: 26px; }
  .footer-brand .brand-name span { display: block; }
  .footer-brand .brand-name .top { font-size: 44px; margin-bottom: 6px; }

  .footer-heading { top: 972px; font-size: 10px; font-weight: 700; letter-spacing: .5px; color: var(--white); }
  .footer-menu a { position: absolute; left: 391px; font-size: 8.8px; color: var(--white); text-decoration: none; }
  .footer-icon {
    width: 18px; height: 18px; border-radius: 50%; background: var(--white);
    display: flex; align-items: center; justify-content: center;
  }
  .footer-text { font-size: 8.8px; line-height: 12px; color: var(--white); }
  .footer-rule { left: 102px; top: 1140px; width: 712px; height: 1px; background: var(--footer-line); }
  .copyright { left: 0; top: 1169px; width: 914px; text-align: center; font-size: 7.3px; color: #ddd; }
</style>
</head>
<body>

<header class="site-header">
  <div class="brand header-brand">
    <div class="brand-name"><span class="top">QUILL 7</span><span>MEADOWS</span></div>
    <div class="brand-dot"></div>
  </div>

  <div class="abs quote-btn">GET A QUOTE</div>

  <svg class="abs call-icon" width="27" height="27" viewBox="0 0 27 27" fill="none" stroke="#1b96d9" stroke-width="1.4" aria-hidden="true">
    <path d="M5 3l4 0 2 6-3 2c1.5 3.5 4 6 7.5 7.5l2-3 6 2v4c0 1.2-1 2-2.2 2C11 23 4 16 3 5.2 3 4 3.8 3 5 3z"/>
    <rect x="14" y="2" width="11" height="8" rx="1"/>
    <path d="M16 5h7M16 7.5h5"/>
  </svg>
  <div class="abs call-label">Call Us</div>
  <div class="abs call-number">07 3900 4417</div>

  <nav class="main-nav">
    <a style="left:431px">HOME</a>
    <a style="left:487px">OUR STORY</a>
    <a style="left:577px">TIPS AND TRICKS</a>
    <a style="left:698px">CONTACT US</a>
    <a style="left:790px">FAQ</a>
  </nav>
</header>

<section class="abs hero" role="img" aria-label="Photo of colleagues working at a laptop on a desk covered with chart printouts and a small potted plant"></section>
<h1 class="abs hero-title">MORTGAGE<br>BROKING</h1>

<section class="abs content-photo" role="img" aria-label="Photo of a team typing on a laptop at a bright office desk with a pen holder and notebooks"></section>
<h2 class="abs section-title">LOREM IPSUM IS SIMPLY DUMMY TEXT</h2>
<div class="abs section-rule"></div>

<p class="abs body-copy" style="top:535px">Sed ut perspiciatis unde omnis iste natus error sit voluptatem accusantium doloremque laudantium, totam rem aperiam, eaque ipsa quae ab illo inventore veritatis et quasi architecto beatae vitae dicta sunt explicabo. Nemo enim ipsam voluptatem quia voluptas sit aspernatur aut odit aut fugit, sed quia consequuntur magni dolores eos qui ratione voluptatem sequi nesciunt. Neque porro quisquam est, qui dolorem ipsum quia dolor sit amet, consectetur, adipisci velit, sed quia non numquam eius modi tempora incidunt ut labore et dolore magnam aliquam quaerat voluptatem. Ut enim ad minima veniam, quis nostrum exercitationem ullam corporis suscipit laboriosam, nisi ut aliquid ex ea commodi consequatur? Quis autem vel eum iure reprehenderit qui in ea voluptate velit esse quam nihil molestiae consequatur, vel illum qui dolorem eum fugiat quo voluptas nulla pariatur?</p>

<p class="abs body-copy" style="top:721px">On the other hand, we denounce with righteous indignation and dislike men who are so beguiled and demoralized by the charms of pleasure of the moment, so blinded by desire, that they cannot foresee the pain and trouble that are bound to ensue; and equal blame belongs to those who fail in their duty through weakness of will,</p>

<p class="abs body-copy" style="top:812px">But in certain circumstances and owing to the claims of duty or the obligations of business it will frequently occur that pleasures have to be repudiated and annoyances accepted. The wise man therefore always holds in these matters to this principle of selection: he rejects pleasures to secure other greater pleasures, or else he endures pains to avoid worse pains.</p>

<footer class="abs site-footer"></footer>

<div class="brand footer-brand">
  <div class="brand-name"><span class="top">QUILL 7</span><span>MEADOWS</span></div>
  <div class="brand-dot"></div>
</div>

<div class="abs footer-heading" style="left:391px">MENU</div>
<nav class="footer-menu">
  <a style="top:1001px">HOME</a>
  <a style="top:1016px">OUR STORY</a>
  <a style="top:1031px">TIPS AND TRICKS</a>
  <a style="top:1046px">CONTACT US</a>
  <a style="top:1061px">FAQ</a>
</nav>

<div class="abs footer-heading" style="left:534px">CONTACT US</div>
<div class="abs footer-icon" style="left:533px;top:1003px">
  <svg width="9" height="9" viewBox="0 0 24 24" aria-hidden="true"><path fill="#2a2a2a" d="M6.6 10.8c1.4 2.8 3.8 5.1 6.6 6.6l2.2-2.2c.3-.3.7-.4 1-.2 1.1.4 2.3.6 3.6.6.6 0 1 .4 1 1V20c0 .6-.4 1-1 1C10.6 21 3 13.4 3 4c0-.6.4-1 1-1h3.5c.6 0 1 .4 1 1 0 1.3.2 2.5.6 3.6.1.3 0 .7-.2 1z"/></svg>
</div>
<div class="abs footer-text" style="left:558px;top:1001px">Call Us<br>0400 555 128</div>
<div class="abs footer-icon" style="left:533px;top:1041px">
  <svg width="9" height="9" viewBox="0 0 24 24" aria-hidden="true"><path fill="#2a2a2a" d="M2 5h20v14H2z"/><path d="M3 6l9 7 9-7" fill="none" stroke="#fff" stroke-width="2"/></svg>
</div>
<div class="abs footer-text" style="left:558px;top:1039px">E mail Us<br>hello@quill7meadows.com.au</div>

<div class="abs footer-heading" style="left:734px">FOLLOW US</div>
<div class="abs footer-icon" style="left:733px;top:1003px"></div>
<div class="abs footer-text" style="left:760px;top:1001px">Like us on<br>PAGEBOARD</div>
<div class="abs footer-icon" style="left:733px;top:1041px"></div>
<div class="abs footer-text" style="left:760px;top:1039px">Follow us on<br>CHIRPLINE</div>
<div class="abs footer-icon" style="left:733px;top:1080px"></div>
<div class="abs footer-text" style="left:760px;top:1078px">Follow us on<br>WORKLINK</div>

<div class="abs footer-rule"></div>
<div class="abs copyright">Copyright © 2020 All Rights Reserved</div>

</body>
</html>
```